Promotion for a free HTML weather widget

skyvelta (http://www.skyvelta-example.com/) is a meteorological service based in Basel, Switzerland.
We offer a free HTML widget that offers weather forecasts for a selected location anywhere on the world for up to seven days (see http://www.skyvelta-example.com/en_GB/weather/forecast/widgetsetup) which can be included in any other website.
To make the widget more popular and well-known, we would like to add a promotional banner for it on our own homepage. The space where the banner will be located is marked red on the attached banner_location.png.
We have received permissions from three websites that are already using our widget to use a screenshot from their website on this banner.
These websites are:
- http://gazette.lumorix-example.ch/ (widget is on the bottom of the page)
- http://www.tonvillage-example.info/
- http://www.valbruna-example.net/
Requirements
Must have
- - Width: 696px
- Height: 150px to 200px
- fits nicely in our website
- uses screenshots of the three aforementioned websites (widget must be visible, other ads on those website must be unrecognisable)
- Text (English) that praises the most important advantages of the widget: it is free to use, worldwide available, easy to integrate, offers valuable weather information to visitors
- Possibility to change the text on our side for translations

```html
<!DOCTYPE html>
<html lang="en">
<head>
<meta charset="utf-8">
<title>HTML Weather Widget – Free</title>
<link href="https://fonts.googleapis.com/css2?family=Arimo:wght@400;700&family=Open+Sans:wght@400;700&display=swap" rel="stylesheet">
<style>
  :root {
    --stage: #2f2f2f;
    --banner-white: #ffffff;
    --banner-fade: #ebebeb;
    --ink: #333333;
    --title-ink: #3a3a3a;
    --icon: #6b6b6b;
    --cta: #a9cdf0;
    --cta-ink: #ffffff;
    --rule: #d6d6d6;
    --wood: #b8864a;
    --widget-bg: #ece8d8;
    --sky: #5aaee6;
    --temp-green: #3cb371;
    --temp-dark: #1f8a55;
    --uv-purple: #9a7be0;
    --radar: #3f8fd6;
    --site-bg: #f6f6f6;
    --link: #2a5db0;
  }
  * { box-sizing: border-box; margin: 0; padding: 0; }
  html, body { width: 1200px; height: 652px; overflow: hidden; }
  body {
    position: relative;
    background: radial-gradient(ellipse at 50% 20%, #454545 0%, var(--stage) 70%);
  }

  .banner {
    position: absolute; left: 192px; top: 209px;
    width: 816px; height: 234px; overflow: hidden;
    background: linear-gradient(90deg, var(--banner-fade) 0%, var(--banner-white) 50%, var(--banner-fade) 100%);
    box-shadow: 0 8px 18px rgba(0,0,0,0.55);
  }

  /* ---------- widget on partner site ---------- */
  .widget {
    position: absolute; left: 0; top: 0; width: 160px; height: 234px;
    background: linear-gradient(180deg, #f1efe6 0%, #e6e2cf 100%);
    border-left: 9px solid var(--wood);
    font-family: "Arimo", Arial, sans-serif;
  }
  .widget__inner {
    position: absolute; left: 0; top: 0; width: 148px; height: 216px;
    background: var(--widget-bg);
    border-right: 2px solid #d8d2bd;
    border-bottom: 2px solid #d8d2bd;
  }
  .widget__row { position: absolute; left: 13px; width: 100px; display: flex; gap: 2px; }
  .widget__row > * { width: 32px; text-align: center; }
  .widget__days { top: 4px; font-size: 12px; color: #7a7a7a; }
  .widget__dates { top: 18px; font-size: 7px; color: #9a9a9a; }
  .widget__icons { top: 32px; }
  .widget__icons svg { width: 31px; height: 27px; }
  .temp {
    height: 18px; line-height: 18px; font-size: 11px; font-weight: 700; color: #fff;
  }
  .temp small { font-size: 6px; font-weight: 400; }
  .widget__max { top: 61px; } .widget__max .temp { background: var(--temp-green); }
  .widget__min { top: 82px; } .widget__min .temp { background: var(--temp-dark); }
  .widget__wind { top: 104px; font-size: 7px; color: #c6c2b2; }
  .widget__uv { top: 134px; } .widget__uv .temp { height: 23px; line-height: 23px; background: var(--uv-purple); }
  .widget__rain { top: 160px; font-size: 8px; color: #6f8fd0; }
  .widget__radar { top: 170px; }
  .widget__radar svg { width: 31px; height: 28px; }
  .widget__brand { position: absolute; left: 16px; top: 201px; font-size: 8px; color: #5b7fb8; }

  /* ---------- partner page ---------- */
  .site {
    position: absolute; left: 160px; top: 0; width: 245px; height: 234px;
    background: var(--site-bg);
    border-left: 5px solid #dcdcdc;
    font-family: "Arimo", Arial, sans-serif;
  }
  .site__mark { position: absolute; left: 6px; top: 12px; width: 24px; height: 24px; background: #4c7a3c; }
  .site__name { position: absolute; left: 46px; top: 14px; font-size: 9px; font-weight: 700; color: var(--link); }
  .site__like { position: absolute; left: 38px; top: 29px; width: 36px; height: 9px; background: #dfe4ee; border: 1px solid #b8c2d6; }
  .site__count { position: absolute; left: 80px; top: 28px; font-size: 7px; color: #555; }
  .site__caption { position: absolute; left: 41px; top: 51px; font-size: 8px; color: #2a5db0; }
  .site__photo {
    position: absolute; left: 42px; top: 58px; width: 186px; height: 152px;
    background: linear-gradient(170deg, #9fb3c8 0%, #7d8a92 35%, #8a7360 65%, #5a4636 100%);
    clip-path: polygon(0 8%, 100% 0, 100% 85%, 0 100%);
  }
  .site__echo {
    position: absolute; left: 228px; top: 48px; width: 22px; height: 150px;
    background: linear-gradient(90deg, rgba(140,140,140,0.45), rgba(240,240,240,0));
  }

  /* ---------- copy ---------- */
  .title-band {
    position: absolute; left: 0; top: 0; width: 100%; height: 37px;
    background: rgba(255,255,255,0.72);
    border-bottom: 1px solid var(--rule);
  }
  .title {
    position: absolute; right: 20px; top: 3px;
    font-family: "Arimo", Arial, sans-serif; font-size: 26px;
    color: var(--title-ink); font-weight: 400;
  }

  .features {
    position: absolute; inset: 0;
    font-family: "Open Sans", Arial, sans-serif; font-size: 16.8px; color: var(--ink);
  }
  .feature { position: absolute; display: flex; align-items: center; gap: 7px; white-space: nowrap; }
  .feature svg { flex: none; }
  .feature--free { left: 469px; top: 79px; }
  .feature--easy { left: 621px; top: 79px; }
  .feature--info { left: 469px; top: 114px; }
  .feature--world { left: 535px; top: 149px; }

  .cta {
    position: absolute; left: 448px; top: 201px; width: 368px; height: 28px;
    background: var(--cta); border-radius: 8px 0 0 8px;
    font-family: "Open Sans", Arial, sans-serif; font-size: 17px; color: var(--cta-ink);
    text-align: center; line-height: 28px;
  }
</style>
</head>
<body>
  <section class="banner">
    <div class="widget">
      <div class="widget__inner">
        <div class="widget__row widget__days"><span>jue</span><span>vie</span><span>sáb</span></div>
        <div class="widget__row widget__dates"><span>12.06</span><span>13.06</span><span>14.06</span></div>
        <div class="widget__row widget__icons">
          <svg viewBox="0 0 31 27"><rect width="31" height="27" fill="var(--sky)"/><circle cx="12" cy="11" r="5" fill="#ffd23a"/><ellipse cx="18" cy="17" rx="9" ry="5" fill="#fff"/></svg>
          <svg viewBox="0 0 31 27"><rect width="31" height="27" fill="var(--sky)"/><circle cx="12" cy="11" r="5" fill="#e86ad0"/><ellipse cx="18" cy="17" rx="9" ry="5" fill="#fff"/></svg>
          <svg viewBox="0 0 31 27"><rect width="31" height="27" fill="var(--sky)"/><circle cx="12" cy="11" r="5" fill="#ffd23a"/><ellipse cx="18" cy="17" rx="9" ry="5" fill="#fff"/></svg>
        </div>
        <div class="widget__row widget__max"><span class="temp">13 <small>°C</small></span><span class="temp">15 <small>°C</small></span><span class="temp">10 <small>°C</small></span></div>
        <div class="widget__row widget__min"><span class="temp">6 <small>°C</small></span><span class="temp">9 <small>°C</small></span><span class="temp">8 <small>°C</small></span></div>
        <div class="widget__row widget__wind"><span>10 km/h</span><span>12 km/h</span><span>14 km/h</span></div>
        <div class="widget__row widget__uv"><span class="temp">11 <small>UV</small></span><span class="temp">11 <small>UV</small></span><span class="temp">10 <small>UV</small></span></div>
        <div class="widget__row widget__rain"><span>&lt;1 mm</span><span>6 mm</span><span>8 mm</span></div>
        <div class="widget__row widget__radar">
          <svg viewBox="0 0 31 28"><rect width="31" height="28" fill="var(--radar)"/><circle cx="15.5" cy="14" r="10" fill="none" stroke="#8fd0ff"/><circle cx="15.5" cy="14" r="5" fill="none" stroke="#8fd0ff"/></svg>
          <svg viewBox="0 0 31 28"><rect width="31" height="28" fill="var(--radar)"/><circle cx="15.5" cy="14" r="10" fill="none" stroke="#8fd0ff"/><circle cx="15.5" cy="14" r="5" fill="none" stroke="#8fd0ff"/></svg>
          <svg viewBox="0 0 31 28"><rect width="31" height="28" fill="var(--radar)"/><circle cx="15.5" cy="14" r="10" fill="none" stroke="#8fd0ff"/><circle cx="15.5" cy="14" r="5" fill="none" stroke="#8fd0ff"/></svg>
        </div>
        <div class="widget__brand">skyvelta-example.com</div>
      </div>
    </div>

    <div class="site">
      <div class="site__mark"></div>
      <div class="site__name">valbruna-example.net</div>
      <div class="site__like"></div>
      <div class="site__count">5 713</div>
      <div class="site__caption">Valbruna y Monte Alto.</div>
      <div class="site__photo" role="img" aria-label="Photo of a white horse in front of a mountain valley"></div>
      <div class="site__echo"></div>
    </div>

    <div class="title-band"><h1 class="title">HTML Weather Widget - Free</h1></div>

    <div class="features">
      <div class="feature feature--free">
        <svg width="18" height="18" viewBox="0 0 18 18"><rect width="18" height="18" rx="2" fill="var(--icon)"/><text x="9" y="14" text-anchor="middle" font-family="Arial, sans-serif" font-size="14" font-weight="700" fill="#fff">$</text></svg>
        <span>Free to use</span>
      </div>
      <div class="feature feature--easy">
        <svg width="26" height="22" viewBox="0 0 26 22"><circle cx="9" cy="13" r="6" fill="none" stroke="var(--icon)" stroke-width="4" stroke-dasharray="3 2"/><circle cx="9" cy="13" r="2" fill="var(--icon)"/><circle cx="20" cy="6" r="4" fill="none" stroke="var(--icon)" stroke-width="3" stroke-dasharray="2 1.5"/></svg>
        <span>Easy to integrate</span>
      </div>
      <div class="feature feature--info">
        <svg width="26" height="20" viewBox="0 0 26 20"><path d="M6 12a5 5 0 0 1 1-9.5A6 6 0 0 1 18 4a4 4 0 0 1 2 8z" fill="none" stroke="var(--icon)" stroke-width="1.6"/><path d="M8 14l-2 4M13 14l-2 4M18 14l-2 4" stroke="var(--icon)" stroke-width="1.6"/></svg>
        <span>Offers valuable weather information</span>
      </div>
      <div class="feature feature--world">
        <svg width="18" height="18" viewBox="0 0 18 18"><rect x="0.5" y="0.5" width="17" height="17" fill="none" stroke="var(--icon)" stroke-dasharray="2 1.5"/><circle cx="9" cy="9" r="5.5" fill="none" stroke="var(--icon)" stroke-width="1.2"/><ellipse cx="9" cy="9" rx="2.3" ry="5.5" fill="none" stroke="var(--icon)"/><path d="M3.5 9h11" stroke="var(--icon)"/></svg>
        <span>Worldwide available</span>
      </div>
    </div>

    <div class="cta">Add it into your own website</div>
  </section>
</body>
</html>
```